Quiet orchard Tarot

I need a logo for my business cards for my tarot reading business. I want the cards to be representative of the (kessel/Lund) tarot cards, similar style/design & feel to these cards. It needs to feature a feather & a reference to birds. Can I please have designs featuring a black bird & a white bird intersecting or relating to each other
Please see image below & use as inspiration I really love this image
Contact Information for Business Card
Quiet Orchard Tarot
Email quietorchardtarot@lumenpost.net
Phone Monica 0493627154 or Denise 0462 735 281

```html
<!DOCTYPE html>
<html lang="en">
<head>
<meta charset="utf-8">
<title>Quiet Orchard Tarot – Business Card</title>
<link rel="stylesheet" href="https://fonts.googleapis.com/css2?family=Crimson+Text:wght@400&family=Pinyon+Script&display=swap">
<style>
  :root {
    --backdrop: #ecebe8;
    --card-teal: #166b80;
    --card-white: #fbfbfa;
    --ink: #1f1f1f;
    --script-teal: #1b7488;
    --badge-black: #0d0d0d;
    --text-white: #ffffff;
    --art-grey: #b9bcbd;
  }
  * { box-sizing: border-box; margin: 0; padding: 0; }
  html, body { width: 872px; height: 1200px; overflow: hidden; }
  body {
    background: var(--backdrop);
    position: relative;
  }
  .card {
    position: absolute;
    width: 360px;
    height: 600px;
    border-radius: 20px;
    box-shadow: 0 6px 18px rgba(0,0,0,0.12);
  }
  .card--front {
    left: 468px;
    top: 300px;
    background: var(--card-teal);
    display: flex;
    flex-direction: column;
    align-items: center;
    justify-content: center;
    gap: 22px;
  }
  .brand-dot {
    width: 150px;
    height: 150px;
    border-radius: 50%;
    background: var(--badge-black);
  }
  .brand-name {
    font-family: "Crimson Text", serif;
    font-size: 26px;
    color: var(--text-white);
    letter-spacing: 0.04em;
  }
  .card--back {
    left: 44px;
    top: 300px;
    background: var(--card-white);
    padding: 190px 0 0 54px;
  }
  .back-title {
    font-family: "Pinyon Script", cursive;
    font-size: 34px;
    color: var(--script-teal);
    line-height: 1;
    margin-bottom: 14px;
  }
  .contact-list {
    list-style: none;
    font-family: "Crimson Text", serif;
    font-size: 17px;
    color: var(--ink);
    line-height: 1.35;
  }
  .back-mark {
    position: absolute;
    left: 50%;
    bottom: 40px;
    transform: translateX(-50%);
    font-family: "Crimson Text", serif;
    font-size: 13px;
    color: var(--ink);
    letter-spacing: 0.05em;
  }
</style>
</head>
<body>
  <section class="card card--back">
    <h1 class="back-title">Quiet Orchard Tarot</h1>
    <ul class="contact-list">
      <li>quietorchardtarot@lumenpost.net</li>
      <li>Monica 0493627154</li>
      <li>Denise 0462 735 281</li>
    </ul>
    <p class="back-mark">Quiet Orchard Tarot</p>
  </section>

  <section class="card card--front">
    <div class="brand-dot"></div>
    <p class="brand-name">Quiet Orchard Tarot</p>
  </section>
</body>
</html>
```